International freight forwarder experienced in perishable handling needs a web design

We need a website designed that will allow us to capture more customers through the website. We would like a visually appealing design that is not so heavy on text. Our business covers the logistics and freight forwarding industries and we have offices in South America and the USA. Our main customers are importers USA, Europe, Asia and Russia and we currently work almost exclusively with perishable products such as fresh cut flowers, fresh exotics fruits, cacao, fresh fish etc. We would like to convey a fresh, modern approach to freight forwarding focusing on concepts such as - time sensitive, anytime-anywhere delivery, innovation, experience, reliability and confidence. Should include links with Plumetta and Worvanet. Our core solutions include: Core Services
*Air Freight
*Ocean Freight
*Warehousing & Distribution
Our industry solutions cover
*Flowers
*FMCG including, fruits, vegetables
*Live animals
*Automotive
*Consumer Goods
*Industrial
*Oil & Gas
*Pharma
* Event logistics
* Project logistics

Target Market(s)

Importers in Europe, USA, Asia, Middle East and Russia

Number of Pages Required

4 page

Font styles to use
Sans Serif

Colors
a1cd39
606060
000000

Requirements
Must have
• Photos of fresh cut flowers, FMCG such as cacao, fresh fish (packaged for shipping), fresh exotic fruits, pharma products (packaged for shipping), oil and gas etc. Internal customer login access
Nice to have
• Photos of cargo shipping carriers and cargo airline carriers. Features similar to those of following website http://www.brolvacargo.com/eng/main/index.jsp?FromURL=web
Should not have
• Too much text, needs to be visually pleasing

```html
<!DOCTYPE html>
<html lang="en">
<head>
<meta charset="utf-8">
<title>Frescura Alliance — Freight Solutions</title>
<link href="https://fonts.googleapis.com/css2?family=Open+Sans:wght@300;400;600;700&family=Playfair+Display:wght@400&display=swap" rel="stylesheet">
<style>
:root{
  --green:#a1cd39;
  --grey:#606060;
  --black:#000000;
  --ink:#333333;
  --btn:#3f3f3f;
  --soft:#eeeef0;
  --footer:#2f2f2f;
  --footer-deep:#232323;
  --muted:#9a9a9a;
}
*{margin:0;padding:0;box-sizing:border-box}
html,body{width:1200px;height:3291px;overflow:hidden}
body{position:relative;font-family:"Open Sans",Arial,sans-serif;color:var(--ink);background:#fff}
.abs{position:absolute}

/* top bar */
.topbar{left:0;top:0;width:1200px;height:40px;background:#2b2b2b}
.social{left:99px;top:11px;display:flex;align-items:center;gap:6px;color:#fff;font-size:11px;font-weight:600}
.social .dot{width:18px;height:18px;border-radius:50%;background:#c9c9c9}
.social .dot.a{background:#e2782b}.social .dot.b{background:#4f6fa8}.social .dot.c{background:#3aa2d8}.social .dot.d{background:#c43a2f}
.search{left:908px;top:8px;width:194px;height:24px;border:1px solid #9a9a9a;border-radius:3px;color:#fff;font-size:11px;padding:4px 8px}
.search svg{position:absolute;right:6px;top:4px}

/* nav */
.nav{left:0;top:40px;width:1200px;height:131px;background:#f3f3f4}
.brand{left:99px;top:96px;display:flex;align-items:center;gap:8px;font-size:21px;font-weight:600;color:var(--grey)}
.brand .mark{width:18px;height:18px;border-radius:50%;background:var(--green)}
.menu{top:40px;left:430px;height:131px;display:flex}
.menu a{display:flex;align-items:center;justify-content:center;height:131px;font-size:15px;color:#333;text-decoration:none;padding:0 22px}
.menu a.active{background:var(--green);color:#fff;width:83px;padding:0}

/* hero */
.hero{left:0;top:171px;width:1200px;height:514px;background:linear-gradient(100deg,#8a6b5c 0%,#c98a6a 30%,#b3262f 48%,#8e1d24 62%,#f0b46a 85%,#f7d08a 100%)}
.arrow{top:401px;width:48px;height:48px;background:var(--green);display:flex;align-items:center;justify-content:center}
.hero-title{left:99px;top:437px;width:489px;height:127px;background:rgba(0,0,0,.45);color:#fff;font-family:"Playfair Display",Georgia,serif;font-size:43px;line-height:54px;padding:10px 28px;letter-spacing:1px}

/* welcome */
.welcome{left:0;top:685px;width:1200px;height:557px;background:var(--soft)}
.map{left:150px;top:730px;width:900px;height:450px;background:radial-gradient(ellipse at center,#e3ead0 0%,#eaeddf 50%,var(--soft) 75%)}
.welcome h2{top:760px;left:0;width:1200px;text-align:center;font-weight:400;font-size:28px;color:#333}
.welcome h3{top:800px;left:0;width:1200px;text-align:center;font-weight:400;font-size:38px;color:var(--green)}
.welcome h3 span{color:#333}
.intro{top:884px;left:210px;width:780px;text-align:center;font-size:12.5px;line-height:16px;color:#555}
.intro p{margin-bottom:8px}
.btn-dark{background:var(--btn);color:#fff;font-size:12px;display:flex;align-items:center;justify-content:center}

/* services */
.service{top:1331px;width:230px}
.service .num{width:72px;height:72px;border-radius:50%;background:#3f3f3f;color:#fff;font-size:26px;display:flex;align-items:center;justify-content:center;margin-left:1px}
.service h4{margin-top:50px;font-size:33px;line-height:36px;font-weight:300;color:var(--green)}
.service h5{margin-top:28px;font-size:17px;font-weight:400;color:#333}
.service p{margin-top:8px;font-size:11.5px;line-height:16px;color:#aaa}
.more{margin-top:36px;display:flex;height:40px;width:154px}
.more .ic{width:44px;background:var(--green);display:flex;align-items:center;justify-content:center}
.more .tx{flex:1;background:var(--btn);color:#fff;font-size:12px;display:flex;align-items:center;justify-content:center}

/* testimonials */
.testi{left:0;top:1887px;width:1200px;height:487px;background:linear-gradient(180deg,#6f8aa0 0%,#4e6479 30%,#3a4a5e 55%,#1f3f6e 75%,#152a4c 100%)}
.testi-title{top:1930px;left:0;width:1200px;text-align:center;color:#fff;font-size:44px;font-weight:300}
.quote{top:1995px;left:0;width:1200px;text-align:center;color:#fff;font-family:"Playfair Display",Georgia,serif;font-size:110px;line-height:110px}
.testi-sub{top:2104px;left:0;width:1200px;text-align:center;color:#fff;font-size:22px}
.testi-text{top:2146px;left:110px;width:980px;text-align:center;color:#fff;font-size:13px;line-height:18px}
.btn-line{top:2255px;left:546px;width:108px;height:40px;border:2px solid #fff;color:#fff;font-size:13px;display:flex;align-items:center;justify-content:center}

/* features */
.feature{top:2448px;width:316px}
.feature h4{font-size:35px;font-weight:300;color:var(--green);line-height:46px}
.feature .photo{margin-top:18px;height:121px}
.feature h5{margin-top:28px;font-size:15.5px;font-weight:400;color:#555}
.feature p{margin-top:8px;font-size:11.5px;line-height:16px;color:#aaa}

/* footer */
.footer{left:0;top:2841px;width:1200px;height:391px;background:var(--footer)}
.fcol{top:2868px;color:#fff}
.fcol h4{font-size:23px;font-weight:400;margin-bottom:22px}
.addr{font-size:11px;line-height:22px;color:#bbb}
.links{list-style:none;width:230px}
.links li{font-size:11px;color:var(--green);padding:8px 0;border-bottom:1px solid #3d3d3d}
.links li::before{content:"› ";color:#bbb}
.tweet{font-size:11px;line-height:16px;color:#bbb;width:230px;margin-bottom:14px}
.tweet b{color:var(--green);font-weight:400}
.field{width:233px;height:35px;background:#3c3c3c;color:#aaa;font-size:12px;padding:9px 10px;margin-bottom:9px}
.field.msg{height:84px}
.submit{width:75px;height:35px;background:var(--green);color:#222;font-size:11px;font-weight:700;display:flex;align-items:center;justify-content:center}
.bottom{left:0;top:3232px;width:1200px;height:59px;background:var(--footer-deep);border-top:1px solid #444}
.copy{left:99px;top:3256px;font-size:11px;color:#888}
</style>
</head>
<body>

<div class="abs topbar"></div>
<div class="abs social">Social Connect : <span class="dot a"></span><span class="dot b"></span><span class="dot c"></span><span class="dot d"></span></div>
<div class="abs search">Search...
  <svg width="16" height="16" viewBox="0 0 16 16"><circle cx="6.5" cy="6.5" r="5" fill="none" stroke="#fff" stroke-width="2"/><line x1="10" y1="10" x2="15" y2="15" stroke="#fff" stroke-width="2.5"/></svg>
</div>

<header class="abs nav"></header>
<div class="abs brand"><span class="mark"></span>Frescura Alliance</div>
<nav class="abs menu">
  <a class="active" href="#">HOME</a>
  <a href="#">ABOUT US</a>
  <a href="#">SERVICES</a>
  <a href="#">CAREERS</a>
  <a href="#">SOLUTIONS</a>
  <a href="#">CONTACT US</a>
</nav>

<section class="abs hero" role="img" aria-label="Red freight truck on a highway at sunset with an industrial skyline"></section>
<div class="abs arrow" style="left:0"><svg width="16" height="20" viewBox="0 0 16 20"><polyline points="12,2 4,10 12,18" fill="none" stroke="#fff" stroke-width="3"/></svg></div>
<div class="abs arrow" style="left:1152px"><svg width="16" height="20" viewBox="0 0 16 20"><polyline points="4,2 12,10 4,18" fill="none" stroke="#fff" stroke-width="3"/></svg></div>
<div class="abs hero-title">SPECIFIC FREIGHT<br>SOLUTIONS</div>

<section class="abs welcome"></section>
<div class="abs map" role="img" aria-label="Faint world map in pale green"></div>
<h2 class="abs" style="top:760px;left:0;width:1200px;text-align:center;font-weight:400;font-size:28px;color:#333">WELCOME TO</h2>
<h3 class="abs" style="top:800px;left:0;width:1200px;text-align:center;font-weight:400;font-size:38px;color:var(--green)">FRESCURA <span style="color:#333">ALLIANCE</span></h3>
<div class="abs intro">
  <p>We envision a fresh cargo market where every shipment is seamlessly tracked and handled, and those insights are translated into actionable decisions by clients.</p>
  <p>We believe that through the leverage of the highest quality cold chain handling, importers will save time and resources without sacrificing freshness or strategic insight.</p>
  <p>We believe that this quality metric can be maintained only by a balance of five factors</p>
  <p>A validated, statistically significant sample of target shippers who are engaged in the process</p>
  <p>Rigorous analysis of robust data sets derived from primary research</p>
  <p>Handling and insights uncovered by industry veterans with client side experience who operate with a passion for the perishable areas they cover</p>
  <p>Content and topics influenced by the most respected international thought leaders</p>
</div>
<div class="abs btn-dark" style="left:531px;top:1147px;width:138px;height:34px">READ MORE</div>

<div class="abs service" style="left:99px">
  <div class="num">01</div><h4>AIR<br>FREIGHT</h4><h5>DOLORE IPSUM</h5>
  <p>Lorem ipsum dolor sit amet, consectetur adipisc elit. Proin ultrices vestibulum velit dum et condimentum metusip dolore</p>
  <div class="more"><span class="ic"><svg width="16" height="16" viewBox="0 0 16 16"><rect x="2" y="4" width="9" height="9" fill="none" stroke="#fff" stroke-width="1.5"/><rect x="5" y="2" width="9" height="9" fill="none" stroke="#fff" stroke-width="1.5"/></svg></span><span class="tx">MORE INFO</span></div>
</div>
<div class="abs service" style="left:355px">
  <div class="num">02</div><h4>SEA<br>FREIGHT</h4><h5>DOLORE IPSUM</h5>
  <p>Lorem ipsum dolor sit amet, consectetur adipisc elit. Proin ultrices vestibulum velit dum et condimentum metusip dolore</p>
  <div class="more"><span class="ic"><svg width="16" height="16" viewBox="0 0 16 16"><rect x="2" y="4" width="9" height="9" fill="none" stroke="#fff" stroke-width="1.5"/><rect x="5" y="2" width="9" height="9" fill="none" stroke="#fff" stroke-width="1.5"/></svg></span><span class="tx">MORE INFO</span></div>
</div>
<div class="abs service" style="left:612px">
  <div class="num">03</div><h4>ROAD<br>FREIGHT</h4><h5>DOLORE IPSUM</h5>
  <p>Lorem ipsum dolor sit amet, consectetur adipisc elit. Proin ultrices vestibulum velit dum et condimentum metusip dolore</p>
  <div class="more"><span class="ic"><svg width="16" height="16" viewBox="0 0 16 16"><rect x="2" y="4" width="9" height="9" fill="none" stroke="#fff" stroke-width="1.5"/><rect x="5" y="2" width="9" height="9" fill="none" stroke="#fff" stroke-width="1.5"/></svg></span><span class="tx">MORE INFO</span></div>
</div>
<div class="abs service" style="left:871px">
  <div class="num">04</div><h4>RAIL<br>FREIGHT</h4><h5>DOLORE IPSUM</h5>
  <p>Lorem ipsum dolor sit amet, consectetur adipisc elit. Proin ultrices vestibulum velit dum et condimentum metusip dolore</p>
  <div class="more"><span class="ic"><svg width="16" height="16" viewBox="0 0 16 16"><rect x="2" y="4" width="9" height="9" fill="none" stroke="#fff" stroke-width="1.5"/><rect x="5" y="2" width="9" height="9" fill="none" stroke="#fff" stroke-width="1.5"/></svg></span><span class="tx">MORE INFO</span></div>
</div>
<div class="abs btn-dark" style="left:531px;top:1799px;width:138px;height:33px">See More</div>

<section class="abs testi" role="img" aria-label="Container ship loaded with cargo at a port under gantry cranes"></section>
<div class="abs testi-title">TESTIMONIALS</div>
<div class="abs quote">“</div>
<div class="abs testi-sub">EU FUGIAT NULLA PARIATUR</div>
<div class="abs testi-text">Lorem ipsum dolor sit amet conse ctetur adipisicing elit, sed do eiusmod tempor incididunt ut labore et dolore magna aliqua. Ut enim ad minim veniam, quis nostrud exercitation ullamco laboris nisi ut aliquip ex ea commodo consequat. Duis aute irure dolor in reprehenderit in voluptate velit esse cillum dolore eu fugiat nulla pariatur. Excepteur sint occaecat cupidatat non proident.</div>
<div class="abs btn-line">SEE ALL</div>

<div class="abs feature" style="left:99px">
  <h4>BEST IN CLASS</h4>
  <div class="photo" role="img" aria-label="Forklift moving stacked cardboard boxes in a warehouse" style="background:linear-gradient(135deg,#5a6470,#c9a36a 55%,#e0c08a)"></div>
  <h5>LOREM IPSUM DOLOR CONSECTETU.</h5>
  <p>Lorem ipsum dolor sit amet, consectetur adipisc elit. Proin ultrices vestibulum velit, bibendum condimentum metusips faucibus sed dolore ipsum commete.</p>
</div>
<div class="abs feature" style="left:441px">
  <h4>OUR FLEET</h4>
  <div class="photo" role="img" aria-label="Row of white trucks driving on a road under a blue sky" style="background:linear-gradient(180deg,#6fa3d8,#cfe0ee 55%,#8f9aa3)"></div>
  <h5>LOREM IPSUM DOLOR CONSECTETU.</h5>
  <p>Lorem ipsum dolor sit amet, consectetur adipisc elit. Proin ultrices vestibulum velit, bibendum condimentum metusips faucibus sed dolore ipsum commete.</p>
</div>
<div class="abs feature" style="left:784px">
  <h4>OUR MISSION</h4>
  <div class="photo" role="img" aria-label="Smiling truck driver in a plaid shirt at the cab window" style="background:linear-gradient(90deg,#8c9096,#d8d8d6 50%,#f2f2f2)"></div>
  <h5>LOREM IPSUM DOLOR CONSECTETU.</h5>
  <p>Lorem ipsum dolor sit amet, consectetur adipisc elit. Proin ultrices vestibulum velit, bibendum condimentum metusips faucibus sed dolore ipsum commete.</p>
</div>

<footer class="abs footer"></footer>
<div class="abs fcol" style="left:99px">
  <h4>Contact</h4>
  <div class="addr">Tarvel Holdings Pty Ltd.<br><br>(Melbourne Office / Head Office)<br>Level 4, Suite 402 / 118 Harlow Street,<br>Melbourne, VIC 3000<br>Phone: (03) 5550 142<br>(Brisbane Office)<br>Shop 2/480 Kessing Road,<br>Moorvale, QLD 4109<br>(07) 5550 2871</div>
</div>
<div class="abs fcol" style="left:358px">
  <h4>Quick Links</h4>
  <ul class="links">
    <li>Lorem ipsum dolor sit</li><li>Amet consectetur</li><li>Praesent vel sem id</li><li>Curabitur hendrerit est</li><li>Aliquam eget erat nec sapien</li><li>Cras id augue nunc</li><li>Sed a nulla urna</li>
  </ul>
</div>
<div class="abs fcol" style="left:612px">
  <h4>Latest Tweets</h4>
  <div class="tweet"><b>@namehere</b> Justoid nonummy laoreet phasellent penatoque in antesque pellus elis eget tincidunt. Nequatdui laorem justo a non tellus laoreet vitae doloreet<br>1 day ago</div>
  <div class="tweet"><b>@namehere</b> Justoid nonummy laoreet phasellent penatoque in antesque pellus elis eget tincidunt. Nequatdui laorem justo a non tellus laoreet vitae doloreet<br>1 day ago</div>
</div>
<div class="abs fcol" style="left:875px">
  <h4>Contact Us</h4>
  <div class="field">Full Name</div>
  <div class="field">Email Address</div>
  <div class="field">Subject</div>
  <div class="field msg">Message</div>
  <div class="submit">SUBMIT</div>
</div>
<div class="abs bottom"></div>
<div class="abs copy">Copyright © 2015 frescura-alliance.com - All Rights Reserved</div>

</body>
</html>
```